Estate Agent/Real Estate valuation tool

We need a design for our our new estate agent valuation tool.

The tool allows users to book a valuation of their house/property with the estate agent, after they choose there property they can then complete their details and choose a booking time.

The mock up of the design we want is attached to this project.(Main Screen)

This also needs to be responsive so the design is easy to use on a mobile device.

Target Market(s)

estate agents

Industry/Entity Type

Real Estate Agent

Number of Pages Required

1 page

Requirements
Must have
• Section 2 and 3 greyed out when user is on step 1
• Section 1 and 3 greyed out when user is on step 2
• Section 1 and 2 greyed out when the user is on step 3
• *** Design must be shown for mobile/ipad and desktop
Nice to have
• Clean and Simple
Should not have
• Dark colours

```html
<!DOCTYPE html>
<html lang="en">
<head>
<meta charset="utf-8">
<title>Harbourline Estates – Book Your Valuation Online</title>
<link rel="stylesheet" href="https://fonts.googleapis.com/css2?family=Open+Sans:wght@400;600;700;800&family=Signika:wght@500&display=swap">
<style>
:root{
  --page-grey:#e4e4e4;
  --brand-blue:#002a78;
  --navy:#0b1240;
  --navy-deep:#07072a;
  --button-blue:#0a3a8c;
  --step-title-active:#1d5f8c;
  --step-title-muted:#1b2d45;
  --panel-grey:#b3b3b3;
  --panel-grey-light:#c4c4c4;
  --row-white:#fafafa;
  --row-grey-end:#e2e2e2;
  --text-dark:#2a2a2a;
  --white:#ffffff;
}
*{box-sizing:border-box;margin:0;padding:0}
html,body{width:1200px;height:845px;overflow:hidden}
body{background:var(--page-grey);font-family:"Open Sans",Arial,sans-serif;position:relative}
.page{position:absolute;left:15px;top:15px;width:1170px;height:815px;background:var(--white)}
.site-header{position:absolute;left:0;top:0;width:1170px;height:132px;background:var(--brand-blue);display:flex;align-items:center;justify-content:center}
.brand-name{color:var(--white);font-family:"Open Sans",Arial,sans-serif;font-weight:800;font-size:34px;letter-spacing:1px;text-transform:uppercase;line-height:1}
.tab-band{position:absolute;left:0;top:132px;width:1170px;height:68px;background:linear-gradient(#ffffff,#e2e2e2)}
.tab-band::after{content:"";position:absolute;left:30px;right:30px;bottom:-22px;height:22px;background:radial-gradient(ellipse at top,rgba(0,0,0,.18),rgba(0,0,0,0) 70%)}
.booking-tab{position:absolute;left:357px;top:13px;width:456px;height:55px;border-radius:4px 4px 0 0;background:linear-gradient(#0c1b4a,#001f6e);display:flex;align-items:center;justify-content:center;gap:16px;color:var(--white);font-size:16px;letter-spacing:.3px}
.step{position:absolute;top:249px;width:350px;height:441px}
.step-1{left:35px}.step-2{left:410px}.step-3{left:785px}
.step-title{height:61px;display:flex;align-items:center;justify-content:center;font-family:"Signika","Open Sans",sans-serif;font-weight:500;font-size:18px;border-radius:3px 3px 0 0}
.step-1 .step-title{background:linear-gradient(#f7f7f7,#e4e4e4);border:1px solid #d4d4d4;color:var(--step-title-active)}
.step-muted .step-title{background:linear-gradient(#c6c6c6,#a9a9a9);color:var(--step-title-muted)}
.field-row{padding:0 20px;display:flex;flex-direction:column;justify-content:center;font-weight:700;font-size:13.5px;color:var(--text-dark)}
.step-1 .field-row{background:linear-gradient(#ffffff,var(--row-grey-end))}
.step-2 .field-row{background:linear-gradient(var(--panel-grey-light),var(--panel-grey));height:103px}
.field-label{margin-bottom:7px;padding-left:3px;text-transform:uppercase}
.text-input{height:27px;border-radius:6px;border:1px solid #8a8a8a;background:#b9b9b9;box-shadow:inset 0 1px 2px rgba(0,0,0,.15)}
.step-1 .text-input{background:var(--white);border-color:#9a9a9a;position:relative}
.search-icon{position:absolute;right:9px;top:4px}
.postcode-row{height:103px}
.address-row{height:69px;font-size:13px}
.action{height:70px;display:flex;align-items:center;justify-content:center}
.step-1 .action{background:#efefef}
.step-muted .action{background:var(--panel-grey)}
.btn{width:311px;height:40px;border-radius:4px;display:flex;align-items:center;justify-content:space-between;padding:0 22px;font-weight:600;font-size:16px;color:var(--white);text-transform:uppercase;box-shadow:0 2px 3px rgba(0,0,0,.35)}
.btn-active{background:linear-gradient(#1450a8,var(--button-blue))}
.btn-muted{background:linear-gradient(#0a0a3a,#03032a);color:#c8c8d6}
.date-strip{height:85px;background:linear-gradient(#c8c8c8,#b0b0b0);display:flex;justify-content:center;align-items:center;gap:3px}
.day{width:43px;height:49px;background:#000;color:var(--white);text-align:center;display:flex;flex-direction:column}
.day-num{font-size:16px;font-weight:700;line-height:19px;margin-top:2px}
.day-month{font-size:8px;font-weight:700;line-height:9px}
.day-name{margin-top:auto;background:#9a9a9a;color:#111;font-size:8.5px;font-weight:800;line-height:12px}
.day-selected{background:var(--navy)}
.day-selected .day-name{background:#7f9ed6}
.slot{height:45px;display:flex;background:linear-gradient(#cbcbcb,#a9a9a9)}
.slot-date{flex:1;display:flex;align-items:center;padding-left:18px;font-weight:700;font-size:13.5px;color:#1a1a1a}
.slot-time{width:90px;background:var(--navy-deep);color:#e6e6ef;font-size:13.5px;display:flex;align-items:center;justify-content:center}
.site-footer{position:absolute;left:0;top:765px;width:1170px;height:50px;background:var(--brand-blue);color:var(--white);text-align:center;font-size:11px;font-weight:700;padding-top:9px;line-height:18px}
.footer-links span{margin:0 13px}
</style>
</head>
<body>
<div class="page">
  <header class="site-header">
    <div class="brand-name">Harbourline Estates</div>
  </header>

  <div class="tab-band">
    <div class="booking-tab">
      <svg width="42" height="40" viewBox="0 0 42 40" aria-hidden="true">
        <rect x="8" y="5" width="30" height="29" rx="2" fill="none" stroke="#fff" stroke-width="2"/>
        <rect x="8" y="5" width="30" height="7" fill="#fff"/>
        <g fill="#fff"><rect x="12" y="2" width="2" height="6"/><rect x="18" y="2" width="2" height="6"/><rect x="24" y="2" width="2" height="6"/><rect x="30" y="2" width="2" height="6"/></g>
        <g stroke="#fff" stroke-width="1"><line x1="11" y1="18" x2="35" y2="18"/><line x1="11" y1="23" x2="35" y2="23"/><line x1="11" y1="28" x2="35" y2="28"/><line x1="17" y1="14" x2="17" y2="31"/><line x1="23" y1="14" x2="23" y2="31"/><line x1="29" y1="14" x2="29" y2="31"/></g>
        <circle cx="8" cy="33" r="6" fill="#0c1b4a" stroke="#fff" stroke-width="1.8"/>
        <path d="M8 30v3h2" stroke="#fff" stroke-width="1.5" fill="none"/>
      </svg>
      <span>BOOK YOUR VALUATION ONLINE</span>
    </div>
  </div>

  <section class="step step-1">
    <h2 class="step-title">STEP 1/3 - PROPERTY DETAILS</h2>
    <div class="field-row postcode-row">
      <label class="field-label">Postcode</label>
      <div class="text-input">
        <svg class="search-icon" width="19" height="19" viewBox="0 0 19 19" aria-hidden="true"><circle cx="7.5" cy="7.5" r="6" fill="none" stroke="#777" stroke-width="1.6"/><line x1="12" y1="12" x2="18" y2="18" stroke="#777" stroke-width="2"/></svg>
      </div>
    </div>
    <div class="field-row address-row">123 TEST STREET</div>
    <div class="field-row address-row">TEST CITY</div>
    <div class="field-row address-row">TEST COUNTY</div>
    <div class="action"><div class="btn btn-active">Proceed<svg width="18" height="20" viewBox="0 0 18 20"><path d="M0 0L18 10L0 20L5 10Z" fill="#fff"/></svg></div></div>
  </section>

  <section class="step step-2 step-muted">
    <h2 class="step-title">STEP 2/3 - YOUR DETAILS</h2>
    <div class="field-row"><label class="field-label">Your Name</label><div class="text-input"></div></div>
    <div class="field-row"><label class="field-label">Your Email</label><div class="text-input"></div></div>
    <div class="field-row"><label class="field-label">Your Contact Number</label><div class="text-input"></div></div>
    <div class="action"><div class="btn btn-muted">Proceed<svg width="18" height="20" viewBox="0 0 18 20"><path d="M0 0L18 10L0 20L5 10Z" fill="#c8c8d6"/></svg></div></div>
  </section>

  <section class="step step-3 step-muted">
    <h2 class="step-title">STEP 3/3 - APPOINTMENT TIME</h2>
    <div class="date-strip">
      <div class="day"><span class="day-num">10</span><span class="day-month">NOV</span><span class="day-name">TODAY</span></div>
      <div class="day day-selected"><span class="day-num">11</span><span class="day-month">NOV</span><span class="day-name">WED</span></div>
      <div class="day"><span class="day-num">12</span><span class="day-month">NOV</span><span class="day-name">THU</span></div>
      <div class="day"><span class="day-num">13</span><span class="day-month">NOV</span><span class="day-name">FRI</span></div>
      <div class="day"><span class="day-num">14</span><span class="day-month">NOV</span><span class="day-name">SAT</span></div>
      <div class="day"><span class="day-num">15</span><span class="day-month">NOV</span><span class="day-name">SUN</span></div>
      <div class="day"><span class="day-num">16</span><span class="day-month">NOV</span><span class="day-name">MON</span></div>
    </div>
    <div class="slot"><span class="slot-date">WEDNESDAY 11TH NOVEMBER</span><span class="slot-time">08:30</span></div>
    <div class="slot"><span class="slot-date">WEDNESDAY 11TH NOVEMBER</span><span class="slot-time">10:30</span></div>
    <div class="slot"><span class="slot-date">WEDNESDAY 11TH NOVEMBER</span><span class="slot-time">12:30</span></div>
    <div class="slot"><span class="slot-date">WEDNESDAY 11TH NOVEMBER</span><span class="slot-time">14:30</span></div>
    <div class="slot"><span class="slot-date">WEDNESDAY 11TH NOVEMBER</span><span class="slot-time">16:30</span></div>
    <div class="action"><div class="btn btn-muted">Confirm Booking<svg width="18" height="20" viewBox="0 0 18 20"><path d="M0 0L18 10L0 20L5 10Z" fill="#c8c8d6"/></svg></div></div>
  </section>

  <footer class="site-footer">
    <div class="footer-links">Terms &amp; Conditions<span>I</span>Security<span>I</span>Privacy Policy</div>
    <div>© 2015 Corporate Name. All Rights Reserved.</div>
  </footer>
</div>
</body>
</html>
```